wolterhagen.info (Physiotherapeut)   //   quellbrand-athletic Webseite
wolterhagen.info (Physiotherapeut) // quellbrand-athletic Webseite
Zielgruppe
Die angesprochene Zielgruppe ist sportlich unterwegs (Sportler jeglicher Sportrichtung). Der externe Shop geht in Richtung Apparels / Kleidung.
Vielleicht wird es aber auch nur eine Physio-Seite und die Apparels kommen im zweiten Schritt - das liegt am Design das man mir präsentiert .... Also legt los ...
(KELVARO wird HOST)
Aufgabenstellung
Mein Name ist Jonathan Wolterhagen ich bin Physiotherapeut / Osteopath (etc).
Die Domain www.wolterhagen.info gehört mir und es würde auch für den Anfang reichen eine digitale Visitenkarte von mir zu erstellen ...
Weiter möchte ich eine Webseite mit dem Namen "quellbrand-athletic" eröffnen. [COM/DE]
Die zu kreierenden Seiten innerhalb der Domain quellbrand-athleti sind:
Main-/LandingPage,
ShopPage (Weiterleitung zu einer externen Webseite),
Impressum,
KooperationsPage (andere Projekte bzw. Webseiten von mir, die in Zukunft kommen).
Design-Vorschläge und umsetzbare / hochladbare Pages (KELVARO) oder NUR Grafiken sind gerne gesehen ...
Die angesprochene Zielgruppe ist sportlich unterwegs (Sportler jeglicher Sportrichtung). Der externe Shop geht in Richtung Apparels.
Die angesprochenen Kreaturen brauchen ein Heim, dass durch ein Schloss repräsentiert werden soll. Evtl. ein Labor. Nicht zu kindlich! Nicht zu düster oder blutig.
Was ich möchte ist: Corporate Identity, eine Webpage (host der Domain wird KELVARO), Logo, etc
Zweiter Schritt wird sein: Grafiken für die Apparels / Klamotten.

```html
<!DOCTYPE html>
<html lang="en">
<head>
<meta charset="utf-8">
<title>wolterhagen – Physiotherapeut</title>
<link href="https://fonts.googleapis.com/css2?family=Cabin:wght@400;600;700&family=Raleway:wght@300;400;600&family=Italianno&display=swap" rel="stylesheet">
<style>
:root{
  --green:#3cc046;
  --green-dark:#2fae3a;
  --green-text:#4db33d;
  --cream:#efeee6;
  --grey-text:#7a7a7a;
  --nav-text:#8a8a7e;
  --ink:#2e3a30;
  --card-top:#2e5a5c;
  --card-bottom:#587a7c;
  --button:#3e9e77;
  --social:#5f86b0;
  --white:#ffffff;
}
*{margin:0;padding:0;box-sizing:border-box}
html,body{width:1086px;height:1200px;overflow:hidden;background:var(--white)}
body{position:relative;font-family:'Cabin',sans-serif}
.abs{position:absolute}
.layer{position:absolute;left:0;top:0;width:1086px;height:1200px;pointer-events:none}
.nowrap{white-space:nowrap}

/* hero */
.hero{left:0;top:0;width:1086px;height:446px;background:var(--cream);overflow:hidden}
.hero-photo{left:470px;top:0;width:616px;height:446px;
  background:linear-gradient(90deg,var(--cream) 0%,rgba(190,205,180,.7) 35%,#8c9a7a 60%,#a86a4a 80%,#6e3a2a 100%)}
.hero-veil{left:0;top:0;width:1086px;height:446px;background:linear-gradient(90deg,var(--cream) 40%,rgba(239,238,230,0) 75%)}
.logo{left:189px;top:19px}
.logo-name{font-family:'Cabin',sans-serif;font-weight:600;font-size:19px;color:var(--green-text);line-height:1}
.logo-sub{font-family:'Raleway',sans-serif;font-size:5.5px;letter-spacing:3.4px;color:var(--green-text);margin-top:3px;white-space:nowrap}
.nav{top:33px;left:0;width:1086px;font-family:'Raleway',sans-serif;font-size:8px;font-weight:600;color:var(--nav-text)}
.nav span{position:absolute;white-space:nowrap}
.nav .active{color:var(--ink)}
.nav-marker{left:489px;top:0;width:67px;height:3px;background:var(--green)}
.social{top:26px;width:22px;height:22px;border-radius:50%;background:var(--social)}
.hero-rule{top:168px;height:1px;background:#cfcfc6}
.hero-dot{left:539px;top:162px;width:12px;height:12px;border-radius:50%;background:var(--ink)}
.headline{left:0;width:1086px;top:208px;text-align:center;font-family:'Raleway',sans-serif;font-weight:300;font-size:27px;letter-spacing:3.4px;color:var(--green-text)}
.hero-copy{left:355px;width:376px;text-align:center;font-family:'Raleway',sans-serif;font-weight:300;font-size:9.3px;line-height:11.6px;color:var(--grey-text)}

/* contact band */
.band{left:0;top:446px;width:1086px;height:148px;background:linear-gradient(90deg,#56b86a 0%,var(--green) 30%,#52c75a 100%)}
.band-photo{left:0;top:446px;width:290px;height:148px;background:linear-gradient(90deg,#3f9a55 0%,#4aae5a 60%,rgba(60,192,70,0) 100%)}
.band-map{left:560px;top:446px;width:526px;height:148px;background:linear-gradient(90deg,rgba(255,255,255,0),rgba(255,255,255,.1))}
.notch{left:533px;top:446px;width:0;height:0;border-left:9px solid transparent;border-right:9px solid transparent;border-top:14px solid var(--cream)}
.ring{top:494px;width:51px;height:51px}
.band-text{color:var(--white);font-size:9px;line-height:16px;font-weight:600;white-space:nowrap}

/* about */
.card{left:187px;top:676px;width:274px;height:337px;background:linear-gradient(170deg,var(--card-top),var(--card-bottom) 60%,#4a6c70)}
.card-frame{left:5px;top:6px;right:5px;bottom:6px;border:1px dashed rgba(255,255,255,.35)}
.card-figure{left:80px;top:155px;width:114px;height:176px;background:linear-gradient(180deg,rgba(25,55,58,.8),rgba(40,75,78,.5));border-radius:40px 40px 4px 4px}
.card-first{left:0;width:274px;top:48px;text-align:center;color:var(--white);font-size:15px}
.card-box{left:67px;top:72px;width:143px;height:32px;border:2px solid var(--white);color:var(--white);font-weight:700;font-size:17px;text-align:center;line-height:28px;letter-spacing:.5px}
.card-role{left:0;width:274px;top:108px;text-align:center;font-family:'Italianno',cursive;font-size:19px;color:var(--white)}
.card-line{left:68px;top:131px;width:139px;height:1px;background:rgba(255,255,255,.35)}
.card-button{left:101px;top:264px;width:79px;height:25px;border-radius:13px;background:var(--button);color:var(--white);font-size:6.5px;font-weight:700;text-align:center;line-height:25px;white-space:nowrap}
.about-copy{left:479px;top:677px;width:425px;font-size:10.6px;line-height:13.4px;color:var(--grey-text)}
.about-copy p{margin-bottom:13.3px}

/* footer */
.footer{left:0;top:1084px;width:1086px;height:116px;background:linear-gradient(180deg,var(--green) 0%,#37b342 100%);border-top:3px solid #45c850}
.footer-base{left:0;top:1188px;width:1086px;height:12px;background:var(--green-dark)}
.f-head{top:1107px;font-size:10.5px;font-weight:700;color:#1f6d27;letter-spacing:.3px;white-space:nowrap}
.f-links{font-size:9.2px;line-height:14px;color:var(--white);white-space:nowrap}
.f-icon{top:1107px}
.footer-mark{left:655px;top:1128px;width:12px;height:12px;border-radius:50%;background:var(--white)}
.copyright{left:766px;top:1128px;font-size:9.2px;line-height:12px;color:var(--white);font-weight:600;white-space:nowrap}
</style>
</head>
<body>

<section class="hero abs">
  <div class="hero-photo abs" role="img" aria-label="Photo of a runner with red hair on a tree-lined running track"></div>
  <div class="hero-veil abs"></div>
  <div class="nav-marker abs"></div>
  <div class="logo abs">
    <div class="logo-name">wolterhagen</div>
    <div class="logo-sub">Physiotherapeut</div>
  </div>
  <nav class="nav abs">
    <span class="active" style="left:509px">HOME</span>
    <span style="left:583px">SHOP</span>
    <span style="left:654px">COOPERATION</span>
    <span style="left:750px">CONTACT US</span>
  </nav>
  <div class="social abs" style="left:839px" role="img" aria-label="Social network link"></div>
  <div class="social abs" style="left:874px;background:#27c0e0" role="img" aria-label="Social network link"></div>

  <div class="hero-rule abs" style="left:333px;width:143px"></div>
  <div class="hero-dot abs"></div>
  <div class="hero-rule abs" style="left:608px;width:144px"></div>

  <h1 class="headline abs">“LOREM IPSUM DOLOR AMET”</h1>
  <p class="hero-copy abs" style="top:273px">Lorem ipsum ad his scripta blandit partiendo eum fastidii accumsan euripidis in, eum liber hendrerit an</p>
  <p class="hero-copy abs" style="top:307px;left:370px;width:346px">ut wisisuscipiantur, quo dicit ridens inciderint iduo mundi lobortis refor midans eu, legimus senserit definie an eos, eu sit tincidunt incorru definitionem, vis mutat affert percipit.</p>
</section>

<section class="layer">
  <div class="band abs"></div>
  <div class="band-photo abs" role="img" aria-label="Photo of a smiling cyclist wearing a helmet"></div>
  <div class="band-map abs" role="img" aria-label="Faint street map of the practice area"></div>
  <div class="notch abs"></div>

  <svg class="ring abs" style="left:249px" viewBox="0 0 51 51"><circle cx="25.5" cy="25.5" r="24.5" fill="none" stroke="#fff" stroke-width="2"/><path d="M25.5 13c-5.5 0-9.5 4-9.5 9.3 0 6.4 9.5 16.7 9.5 16.7s9.5-10.3 9.5-16.7c0-5.3-4-9.3-9.5-9.3z" fill="none" stroke="#fff" stroke-width="2.4"/></svg>
  <div class="band-text abs" style="left:326px;top:506px">Linden Street 42,<br>City Country</div>

  <svg class="ring abs" style="left:487px" viewBox="0 0 51 51"><circle cx="25.5" cy="25.5" r="24.5" fill="none" stroke="#fff" stroke-width="2"/><path d="M19 15c2-1 3 0 4 2l1.5 3c.5 1.3 0 2.3-1 3l-1.2.8c.8 2.3 2.4 4.6 4.6 6.3l1.1-.9c1-.8 2-.8 3 0l2.7 2.2c1.2 1 1.2 2.2.2 3.3-2 2.3-4.6 2.8-7.4 1-4.6-3-8-8-8.8-13.4-.4-3 .4-5.8 1.3-8.3z" fill="#fff"/></svg>
  <div class="band-text abs" style="left:563px;top:512px">+49-30-5550192</div>

  <svg class="ring abs" style="left:689px" viewBox="0 0 51 51"><circle cx="25.5" cy="25.5" r="24.5" fill="none" stroke="#fff" stroke-width="2"/><rect x="14" y="17" width="23" height="17" rx="1.5" fill="none" stroke="#fff" stroke-width="2"/><path d="M16 21h19M18 25h15M18 28h15M18 31h15" stroke="#fff" stroke-width="1.4"/></svg>
  <div class="band-text abs" style="left:764px;top:508px;font-weight:400">email@wolterhagen.info</div>
</section>

<section class="layer">
  <div class="card abs" role="img" aria-label="Portrait of the physiotherapist against a cloudy sky">
    <div class="card-frame abs"></div>
    <div class="card-figure abs"></div>
    <div class="card-first abs">Jonathan</div>
    <div class="card-box abs">Wolterhagen</div>
    <div class="card-role abs">Physiotherapeut</div>
    <div class="card-line abs"></div>
    <div class="card-button abs">CONTACT ME</div>
  </div>

  <div class="about-copy abs">
    <p>Lorem ipsum ad his scripta blandit partiendo eum fastidii accumsan euripidis in, eum liber hendrerit an ut wisisuscipiantur, quo dicit ridens inciderint id. Quo mundi lobortis refor midans eu, legimus senserit definie an eos, eu sit tincidunt incorru definitionem, vis mutat affert percipit.</p>
    <p>Ad his scripta blandit partiendo eum fastidii accumsan euripidis in, eum liber hendrerit an ut wisisuscipiantur, quo dicit ridens inciderint id. Quo mundi lobortis refor midans eu, legimus senserit definie an eos, eu sit tincidunt incorru definitionem, vis mutat affert percipit ipsum ad his scripta blandit partiendo eum fastidii accumsan euripidis in, eum liber hendrerit an ut wisisuscipiantur, quo dicit ridens inciderint id. Quo mundi lobortis refor midans eu, legimus senserit definie an eos, eu sit tincidunt incorru definitionem, vis mutat affert percipit.</p>
    <p>Lorem ipsum ad his scripta blandit partiendo eum fastidii accumsan euripidis in, eum liber hendrerit an ut wisisuscipiantur, quo dicit ridens inciderint id. Quo mundi lobortis refor midans eu, legimus senserit definie an eos, eu sit tincidunt incorru definitionem, vis mutat affert percipit.</p>
    <p>Scripta blandit partiendo eum fastidii accumsan euripidis in, eum liber hendrerit an ut wisisuscipiantur, quo dicit ridens inciderint id. Quo mundi lobortis refor midans eu, legimus senserit definie an eos, eu sit tincidunt incorru definitionem, vis mutat affert percipit.</p>
    <p>Lorem ipsum ad his scripta blandit partiendo eum fastidii accumsan euripidis in, eum liber hendrerit an ut wisisuscipiantur, quo dicit ridens inciderint id. Quo mundi lobortis refor midans eu.</p>
  </div>
</section>

<footer class="layer">
  <div class="footer abs"></div>
  <div class="footer-base abs"></div>

  <svg class="f-icon abs" style="left:199px" width="10" height="13" viewBox="0 0 10 13"><path d="M5 1C2.8 1 1.2 2.6 1.2 4.7 1.2 7.3 5 12 5 12s3.8-4.7 3.8-7.3C8.8 2.6 7.2 1 5 1z" fill="none" stroke="#1f6d27" stroke-width="1.4"/></svg>
  <div class="f-head abs" style="left:215px">CONTACT US :</div>
  <div class="f-links abs" style="left:215px;top:1132px">email@wolterhagen.info<br>Phone: 555-014-2290</div>

  <svg class="f-icon abs" style="left:363px" width="15" height="12" viewBox="0 0 15 12"><rect x="1" y="1.5" width="13" height="9.5" fill="none" stroke="#1f6d27" stroke-width="1.4"/><path d="M1 4.5h13" stroke="#1f6d27" stroke-width="1.4"/></svg>
  <div class="f-head abs" style="left:385px">ABOUT US :</div>
  <div class="f-links abs" style="left:385px;top:1130px">About Us</div>

  <svg class="f-icon abs" style="left:511px" width="11" height="12" viewBox="0 0 11 12"><circle cx="5.5" cy="3.5" r="2.8" fill="#1f6d27"/><path d="M.5 12c0-3.3 2.2-5 5-5s5 1.7 5 5z" fill="#1f6d27"/></svg>
  <div class="f-head abs" style="left:528px">SERVICE :</div>
  <div class="f-links abs" style="left:528px;top:1132px">Shop<br>Cooperation</div>

  <div class="footer-mark abs"></div>
  <div class="copyright abs">Copyright wolterhagen<br>2015. All rights reserved.</div>
</footer>

</body>
</html>
```